Brightholm painting

Am looking for a lawn sign design for my paintings company.
I also attached my business card a example

Phone number of the business +1(431)572-8846
Key words:Free estimates|pressure washing |Residential| Commercial | Interior | Exterior

```html
<!DOCTYPE html>
<html lang="en">
<head>
<meta charset="utf-8">
<title>Brightholm Painting – Lawn Sign</title>
<link rel="stylesheet" href="https://fonts.googleapis.com/css2?family=Poppins:wght@400;500&family=Open+Sans:ital@1&family=Roboto+Condensed:wght@700&display=swap">
<style>
  :root {
    --sign-black: #000000;
    --brand-blue: #00a7e1;
    --ink-white: #ffffff;
    --lawn-light: #6cc93a;
    --lawn-deep: #2f9a30;
  }
  * { margin: 0; padding: 0; box-sizing: border-box; }
  html, body {
    width: 1200px; height: 900px; overflow: hidden;
    background: var(--sign-black);
  }
  .lawn-sign {
    position: relative;
    width: 1200px; height: 900px;
    background: var(--sign-black);
    font-family: "Poppins", sans-serif;
  }
  .brand-name {
    position: absolute; left: 0; right: 0; top: 48px;
    text-align: center;
    color: var(--brand-blue);
    font-weight: 500;
    text-transform: uppercase;
    line-height: 1;
  }
  .brand-name__primary {
    display: block;
    font-size: 76px;
    letter-spacing: 4px;
  }
  .brand-name__secondary {
    display: block;
    margin-top: 14px;
    font-size: 60px;
    letter-spacing: 24px;
    padding-left: 24px;
  }
  .hero-glow {
    position: absolute; left: 120px; top: 200px;
    width: 960px; height: 30px;
  }
  .hero-photo {
    position: absolute; left: 98px; top: 222px;
    width: 1003px; height: 392px;
    background: linear-gradient(180deg, var(--lawn-light) 0%, var(--lawn-deep) 100%);
  }
  .services {
    position: absolute; left: 0; right: 0; top: 637px;
    text-align: center;
    color: var(--brand-blue);
    font-weight: 400;
    font-size: 42px;
    line-height: 50px;
    text-transform: uppercase;
  }
  .services__row { display: block; white-space: nowrap; }
  .services__divider { color: var(--ink-white); }
  .call-prompt {
    position: absolute; left: 0; right: 0; top: 779px;
    text-align: center;
    color: var(--ink-white);
    font-family: "Open Sans", sans-serif;
    font-style: italic;
    font-size: 18px;
  }
  .contact-line {
    position: absolute; left: 81px; right: 81px; top: 812px;
    display: flex; align-items: center; justify-content: space-between;
  }
  .contact-line__rule {
    width: 317px; height: 2px; background: var(--ink-white);
  }
  .contact-line__phone {
    color: var(--ink-white);
    font-family: "Roboto Condensed", sans-serif;
    font-weight: 700;
    font-size: 49px;
    line-height: 56px;
    letter-spacing: -1px;
  }
</style>
</head>
<body>
  <main class="lawn-sign">
    <h1 class="brand-name">
      <span class="brand-name__primary">Brightholm</span>
      <span class="brand-name__secondary">Painting</span>
    </h1>

    <svg class="hero-glow" viewBox="0 0 960 30" aria-hidden="true">
      <defs>
        <radialGradient id="glowHalo" cx="50%" cy="70%" r="50%">
          <stop offset="0%" stop-color="#ff9a2e" stop-opacity="0.9"/>
          <stop offset="100%" stop-color="#ff9a2e" stop-opacity="0"/>
        </radialGradient>
      </defs>
      <ellipse cx="480" cy="22" rx="480" ry="12" fill="url(#glowHalo)"/>
      <ellipse cx="486" cy="22" rx="110" ry="4" fill="#fff6d8"/>
    </svg>

    <div class="hero-photo" role="img" aria-label="Photo of a fresh green lawn in warm evening light"></div>

    <p class="services">
      <span class="services__row">Free Estimates <span class="services__divider">|</span> Pressure Washing</span>
      <span class="services__row">Residential <span class="services__divider">|</span> Commercial <span class="services__divider">|</span> Interior <span class="services__divider">|</span> Exterior</span>
    </p>

    <p class="call-prompt">Call to find out more</p>

    <div class="contact-line">
      <span class="contact-line__rule"></span>
      <span class="contact-line__phone">+1(431)572-8846</span>
      <span class="contact-line__rule"></span>
    </div>
  </main>
</body>
</html>
```